Business Card Design for New Game Studio

We need a business card design. We are a new company developing innovative mobile and platform games.

I would like to see very innovative design thats brings out the company's goal and direction.

My Company's goal and direction is to "Evolve the way of gaming, Bring fun and entertainment to all gamers"

Please do use our company logo which I have attached to be included in the design.

Please put in details for name, title, contacts etc ... be creative !!!

Reason: Company logo redesign. Awaiting it. Thanks

Hi all Please do wait for my updated company logo. Thanks

Reason: Still waiting on new company logo. Thanks all

Hi All Designers .... Sorry for the long wait... Please see the new file for my new company logo uploaded. Waiting to see all your creative design. Cheers

Hi All .... Please do not just mass send a whole bunch of similar designs .... Would like to see quality instead of quantity Cheers

Entertainment

```html
<!DOCTYPE html>
<html lang="en">
<head>
<meta charset="utf-8">
<title>Novaplay Studio – Business Card</title>
<link href="https://fonts.googleapis.com/css2?family=Cinzel:wght@700&family=Open+Sans:wght@400&family=Roboto+Condensed:wght@400;700&display=swap" rel="stylesheet">
<style>
  :root{
    --lime:#ccff00;
    --lime-deep:#a8d000;
    --ink:#161616;
    --charcoal:#2b2b2b;
    --divider:#1e9be0;
    --paper:#ffffff;
    --text-dark:#111111;
  }
  *{margin:0;padding:0;box-sizing:border-box}
  html,body{width:1012px;height:1200px;overflow:hidden;background:var(--paper)}
  .canvas{position:relative;width:1012px;height:1200px;overflow:hidden}

  /* Front face */
  .card-front{position:absolute;left:0;top:0;width:1012px;height:593px;
    background:linear-gradient(180deg,var(--lime) 0%,var(--lime-deep) 100%)}
  .front-shapes{position:absolute;left:0;top:0}
  .brand-header{position:absolute;left:277px;top:16px;width:697px;height:117px;
    background:var(--ink);border-radius:10px;display:flex;align-items:center;justify-content:center;gap:14px}
  .brand-name{font-family:"Roboto Condensed",sans-serif;font-weight:700;font-size:56px;color:var(--lime);letter-spacing:1px}
  .side-mark{position:absolute;left:60px;top:230px;width:110px;height:110px;background:var(--lime)}

  .person{position:absolute;left:353px;top:204px}
  .person-name{font-family:"Cinzel",serif;font-weight:700;font-size:40px;color:var(--text-dark);line-height:1;letter-spacing:.5px}
  .person-title{font-family:"Cinzel",serif;font-weight:700;font-size:17px;color:#333;margin-top:5px;letter-spacing:1px}

  .contacts{position:absolute;left:552px;top:344px;font-family:"Roboto Condensed",sans-serif;font-size:29px;color:var(--text-dark)}
  .contact-row{display:grid;grid-template-columns:40px 130px 230px;align-items:center;height:54px}
  .contact-icon{width:34px;height:34px}
  .contact-label{text-align:right;white-space:nowrap}
  .contact-value{padding-left:29px;white-space:nowrap}

  .address-bar{position:absolute;left:214px;top:519px;width:774px;height:74px;background:var(--ink);
    border-radius:8px 8px 0 0;display:flex;align-items:center;justify-content:center;
    font-family:"Open Sans",sans-serif;font-size:23px;color:var(--paper)}

  .divider{position:absolute;left:0;top:593px;width:1012px;height:13px;background:var(--divider)}

  /* Back face */
  .card-back{position:absolute;left:0;top:606px;width:1012px;height:594px;
    background:linear-gradient(180deg,var(--lime) 0%,var(--lime-deep) 100%)}
  .back-shapes{position:absolute;left:0;top:0}
  .back-brand{position:absolute;left:34px;top:450px;display:flex;align-items:center;gap:12px}
  .back-brand .brand-name{color:var(--paper);font-size:52px}
</style>
</head>
<body>
<main class="canvas">
  <section class="card-front">
    <svg class="front-shapes" width="1012" height="593" viewBox="0 0 1012 593" aria-hidden="true">
      <rect x="0" y="0" width="153" height="593" fill="var(--ink)"/>
      <rect x="153" y="133" width="62" height="329" fill="var(--ink)"/>
      <rect x="214" y="105" width="48" height="383" rx="8" fill="var(--ink)"/>
      <rect x="989" y="105" width="30" height="383" rx="8" fill="var(--ink)"/>
    </svg>
    <div class="side-mark"></div>
    <header class="brand-header">
      <span class="brand-name">Novaplay Studio</span>
    </header>

    <div class="person">
      <div class="person-name">Marcus Hale</div>
      <div class="person-title">Business Development Manager</div>
    </div>

    <div class="contacts">
      <div class="contact-row">
        <svg class="contact-icon" viewBox="0 0 34 34" aria-hidden="true">
          <rect x="9" y="2" width="16" height="30" rx="2.5" fill="none" stroke="var(--text-dark)" stroke-width="3"/>
          <rect x="14" y="26" width="6" height="2" fill="var(--text-dark)"/>
        </svg>
        <span class="contact-label">Mobile:</span>
        <span class="contact-value">+65 800-55-0199</span>
      </div>
      <div class="contact-row">
        <svg class="contact-icon" viewBox="0 0 34 34" aria-hidden="true">
          <rect x="2" y="7" width="30" height="20" fill="var(--text-dark)"/>
          <path d="M3 8 L17 19 L31 8 M3 26 L13 16 M31 26 L21 16" fill="none" stroke="var(--lime)" stroke-width="2"/>
        </svg>
        <span class="contact-label">E-mail:</span>
        <span class="contact-value">hi@novaplay.com</span>
      </div>
      <div class="contact-row">
        <svg class="contact-icon" viewBox="0 0 34 34" aria-hidden="true">
          <circle cx="17" cy="17" r="15" fill="var(--text-dark)"/>
          <path d="M10 9 Q15 8 16 13 Q12 16 9 14 Z M19 16 Q25 15 26 21 Q23 27 19 26 Q20 21 19 16 Z" fill="var(--lime)"/>
        </svg>
        <span class="contact-label">Website:</span>
        <span class="contact-value">www.novaplay.com</span>
      </div>
    </div>

    <div class="address-bar">1420, Harbor Lane, Lakeview, United States, 90210</div>
  </section>

  <div class="divider"></div>

  <section class="card-back">
    <svg class="back-shapes" width="1012" height="594" viewBox="0 0 1012 594" aria-hidden="true">
      <defs>
        <radialGradient id="backGlow" cx="520" cy="330" r="360" gradientUnits="userSpaceOnUse">
          <stop offset="0" stop-color="#5e5e5e"/>
          <stop offset="0.6" stop-color="var(--charcoal)"/>
          <stop offset="1" stop-color="#262626"/>
        </radialGradient>
      </defs>
      <polygon points="0,0 221,0 716,594 0,594" fill="url(#backGlow)"/>
    </svg>
    <div class="back-brand">
      <span class="brand-name">Novaplay Studio</span>
    </div>
  </section>
</main>
</body>
</html>
```